PowerPoint template for a tech startup

We need a PowerPoint template with a title slide, text slide, section slide, and thank you slide.
Our application helps engineering teams to be more productive. We would love a design that is slick, sophisticated, and consistent with our brand. (see more at www.quenvomi.io or attached files)
By the way (not a requirement), Quenvo means lighthouse in Greek.
Also, here is the font we used (not required) - https://fonts.trelvanic.com/fonts/league-gothic

Other font styles liked:
• https://fonts.trelvanic.com/fonts/league-gothic

```html
<!DOCTYPE html>
<html lang="en">
<head>
<meta charset="utf-8">
<title>Quenvo Presentation Template</title>
<link rel="stylesheet" href="https://fonts.googleapis.com/css2?family=Montserrat:wght@300;400;800;900&display=swap">
<style>
  :root {
    --navy: #12496d;
    --orange: #ee5a1c;
    --purple: #7d6bf6;
    --purple-soft: #a79cfb;
    --pink: #f5718f;
    --grey-text: #6d7378;
    --rule: #e6e8ec;
    --page: #ffffff;
    --canvas: #ffffff;
  }
  * { margin: 0; padding: 0; box-sizing: border-box; }
  html, body { width: 1200px; height: 2760px; overflow: hidden; background: var(--canvas); }
  body { position: relative; font-family: "Montserrat", Arial, sans-serif; }

  .slide {
    position: absolute; left: 11px; width: 1176px; height: 662px;
    background: var(--page); overflow: hidden;
    box-shadow: 0 2px 6px rgba(0,0,0,0.22);
  }
  .slide--title   { top: 13px; }
  .slide--text    { top: 704px; }
  .slide--divider { top: 1393px; }
  .slide--closing { top: 2084px; }
  .slide--title, .slide--closing {
    background: linear-gradient(180deg, #ffffff 0%, #f6f6f7 55%, #e9e9eb 100%);
  }

  .wordmark {
    position: absolute; display: flex; align-items: center; gap: 8px;
    font-weight: 800; color: var(--navy); letter-spacing: 0.5px;
  }
  .wordmark__dot { width: 12px; height: 12px; background: var(--orange); border-radius: 50%; }
  .wordmark--large { font-size: 34px; }
  .wordmark--small { font-size: 20px; }
  .wordmark--small .wordmark__dot { width: 8px; height: 8px; }

  .display {
    position: absolute; left: 61px; font-weight: 900; color: var(--navy);
    font-size: 46px; line-height: 64px; letter-spacing: 0.5px;
  }
  .lede {
    position: absolute; left: 57px; top: 445px; width: 520px;
    font-size: 12px; line-height: 19px; color: var(--orange); font-weight: 400;
  }
  .site-link {
    position: absolute; left: 62px; top: 592px; font-size: 10px; color: var(--purple);
  }
  .illustration { position: absolute; }

  /* Text slide */
  .heading {
    position: absolute; left: 59px; top: 62px; font-size: 40px; font-weight: 900; color: var(--navy);
  }
  .heading-bars { position: absolute; left: 60px; top: 122px; display: flex; gap: 5px; }
  .heading-bars span { height: 5px; border-radius: 3px; }
  .heading-bars .bar-a { width: 35px; background: var(--purple); }
  .heading-bars .bar-b { width: 19px; background: var(--pink); }
  .subheading {
    position: absolute; left: 59px; top: 192px; font-size: 28px; font-weight: 900; color: var(--purple);
  }
  .body-copy { position: absolute; left: 59px; top: 253px; width: 1050px; }
  .body-copy p {
    font-size: 14.3px; line-height: 21px; color: var(--grey-text); font-weight: 300;
    margin-bottom: 21px;
  }
  .footer-note { position: absolute; left: 59px; top: 608px; font-size: 10px; color: var(--navy); }
  .footer-rule { position: absolute; left: 310px; top: 614px; width: 790px; height: 1px; background: var(--rule); }
  .page-number {
    position: absolute; left: 1131px; top: 598px; width: 45px; height: 32px;
    background: var(--purple); color: #fff; font-size: 12px;
    border-radius: 16px 0 0 16px; display: flex; align-items: center; justify-content: center;
  }

  /* Divider */
  .subtitle { position: absolute; left: 57px; top: 533px; font-size: 13px; color: var(--orange); }

  /* Closing */
  .thanks { position: absolute; left: 60px; top: 330px; font-size: 64px; font-weight: 900; color: var(--navy); }
  .contact-name { position: absolute; left: 73px; top: 495px; font-size: 24px; font-weight: 900; color: var(--purple); }
  .contact-row {
    position: absolute; left: 60px; display: flex; align-items: center; gap: 20px;
    font-size: 12px; color: #333;
  }
  .contact-row svg { width: 24px; height: 24px; }
</style>
</head>
<body>

<section class="slide slide--title">
  <div class="wordmark wordmark--large" style="left:70px;top:70px;"><span>QUENVO</span><span class="wordmark__dot"></span></div>
  <h1 class="display" style="top:238px;">The Connected<br>Engineering<br>Operations Platform</h1>
  <p class="lede">Quenvo AI connects the dots between your engineering data sources – ticketing, source control, CI/CD, and more – giving unprecedented visibility and insight into your engineering processes.</p>
  <p class="site-link">www.quenvomi.io</p>
  <svg class="illustration" style="left:643px;top:180px;" width="470" height="390" viewBox="0 0 470 390" role="img" aria-label="Illustration of a developer working on a laptop at a desk with floating app icons">
    <defs><linearGradient id="blobA" x1="0" y1="0" x2="1" y2="1"><stop offset="0" stop-color="#a79cfb"/><stop offset="1" stop-color="#6e5cf2"/></linearGradient></defs>
    <path d="M40 160 C10 240 70 340 180 370 C300 400 420 340 450 220 C475 120 420 60 330 80 C260 95 200 50 130 80 C80 100 55 125 40 160 Z" fill="url(#blobA)"/>
  </svg>
</section>

<section class="slide slide--text">
  <h2 class="heading">Text Slide</h2>
  <div class="heading-bars"><span class="bar-a"></span><span class="bar-b"></span></div>
  <div class="wordmark wordmark--small" style="left:1020px;top:62px;"><span>QUENVO</span><span class="wordmark__dot"></span></div>
  <h3 class="subheading">The Connected Engineering Operations Platform</h3>
  <div class="body-copy">
    <p>A wonderful serenity has taken possession of my entire soul, like these sweet mornings of spring which I enjoy with my whole heart. I am alone, and feel the charm of existence in this spot, which was created for the bliss of souls like mine.</p>
    <p>A wonderful serenity has taken possession of my entire soul, like these sweet mornings of spring which I enjoy with my whole heart. I am alone, and feel the charm of existence in this spot, which was created for the bliss of souls like mine.</p>
    <p>A wonderful serenity has taken possession of my entire soul, like these sweet mornings of spring which I enjoy with my whole heart. I am alone, and feel the charm of existence in this spot, which was created for the bliss of souls like mine.</p>
    <p>A wonderful serenity has taken possession of my entire soul, like these sweet mornings of spring which I enjoy with my whole heart. I am alone, and feel the charm of existence in this spot, which was created for the bliss of souls like mine.</p>
    <p>A wonderful serenity has taken possession of my entire soul, like these sweet mornings of spring which I enjoy with my whole heart. I am alone, and feel the charm of existence in this spot, which was created for the bliss of souls like mine.</p>
  </div>
  <p class="footer-note">© 2022 QUENVO. All rights reserved</p>
  <div class="footer-rule"></div>
  <div class="page-number">2</div>
</section>

<section class="slide slide--divider">
  <svg class="illustration" style="left:0;top:0;" width="1176" height="662" viewBox="0 0 1176 662" role="img" aria-label="Isometric illustration of a laptop with data charts and small figures analysing business metrics">
    <path d="M348 0 H1176 V270 C1120 280 1090 340 1080 420 C1060 520 980 560 880 540 C800 520 720 540 660 520 C580 495 560 420 580 340 C595 270 640 215 600 170 C560 130 480 170 420 150 C370 130 360 60 348 0 Z" fill="#7d6bf6"/>
    <rect x="580" y="20" width="520" height="500" rx="14" fill="#e9ecf6" opacity="0.55"/>
  </svg>
  <div class="wordmark wordmark--large" style="left:70px;top:285px;"><span>QUENVO</span><span class="wordmark__dot"></span></div>
  <h2 class="display" style="top:396px;">Divider Title<br>Goes Here</h2>
  <p class="subtitle">Subtitle Here</p>
</section>

<section class="slide slide--closing">
  <div class="wordmark wordmark--large" style="left:70px;top:66px;"><span>QUENVO</span><span class="wordmark__dot"></span></div>
  <h2 class="thanks">Thank you</h2>
  <p class="contact-name">Name Here</p>
  <div class="contact-row" style="top:542px;">
    <svg viewBox="0 0 24 24" fill="none" stroke="#7d6bf6" stroke-width="1.6"><path d="M5 3h4l2 5-2.5 1.5a11 11 0 0 0 6 6L16 13l5 2v4a2 2 0 0 1-2 2A17 17 0 0 1 3 5a2 2 0 0 1 2-2z"/></svg>
    <span>081333xxxxxx / 082233xxxxx</span>
  </div>
  <div class="contact-row" style="top:574px;">
    <svg viewBox="0 0 24 24" fill="none" stroke="#7d6bf6" stroke-width="1.6"><path d="M3 9l2-5h14l2 5M3 9h18M3 9v2a3 3 0 0 0 6 0 3 3 0 0 0 6 0 3 3 0 0 0 6 0V9M5 13v8h14v-8M10 21v-5h4v5"/></svg>
    <span>www.quenvomi.io</span>
  </div>
  <svg class="illustration" style="left:643px;top:180px;" width="470" height="390" viewBox="0 0 470 390" role="img" aria-label="Illustration of a developer working on a laptop at a desk with floating app icons">
    <defs><linearGradient id="blobB" x1="0" y1="0" x2="1" y2="1"><stop offset="0" stop-color="#a79cfb"/><stop offset="1" stop-color="#6e5cf2"/></linearGradient></defs>
    <path d="M40 160 C10 240 70 340 180 370 C300 400 420 340 450 220 C475 120 420 60 330 80 C260 95 200 50 130 80 C80 100 55 125 40 160 Z" fill="url(#blobB)"/>
  </svg>
</section>

</body>
</html>
```